I am a home builder and developer

I would like some sort of architectural design like a pencil type of drawing of a house but want it to be professional looking and two sided.

Simply I am a custom home builder and land developer. I would like a new design other than what I have now that's what I thought y'all did. I like mostly black maybe with an pencil type of drawing of a house. Like an architectural look.

Industry/Entity Type

Home Builder

```html
<!DOCTYPE html>
<html lang="en">
<head>
<meta charset="UTF-8">
<title>Corvale Edifício Inc — Business Card</title>
<link href="https://fonts.googleapis.com/css2?family=Audiowide&family=Orbitron:wght@500&display=swap" rel="stylesheet">
<style>
  :root {
    --page: #ffffff;
    --card-core: #050505;
    --card-mid: #161616;
    --card-edge: #a8a8a8;
    --accent: #f2e33a;
  }
  html, body {
    margin: 0;
    padding: 0;
    width: 1090px;
    height: 1200px;
    overflow: hidden;
    background: var(--page);
  }
  .canvas {
    position: relative;
    width: 1090px;
    height: 1200px;
  }
  .card {
    position: absolute;
    left: 4px;
    width: 1082px;
    border-radius: 90px;
    background: radial-gradient(ellipse at center, var(--card-core) 35%, var(--card-mid) 62%, #3a3a3a 82%, var(--card-edge) 100%);
    overflow: hidden;
  }
  .card--front { top: 0; height: 575px; }
  .card--back { top: 625px; height: 575px; }

  .emblem {
    position: absolute;
    left: 287px;
    top: 103px;
    width: 370px;
    height: 370px;
  }
  .emblem-name {
    position: absolute;
    left: 287px;
    top: 103px;
    width: 370px;
    height: 370px;
    display: flex;
    align-items: center;
    justify-content: center;
    text-align: center;
    font-family: "Audiowide", sans-serif;
    font-size: 40px;
    line-height: 1.15;
    color: var(--accent);
  }

  .company-name {
    position: absolute;
    left: 0;
    right: 0;
    top: 136px;
    margin: 0;
    text-align: center;
    font-family: "Audiowide", sans-serif;
    font-weight: 400;
    font-size: 60px;
    letter-spacing: 5px;
    color: var(--accent);
  }
  .contact {
    position: absolute;
    left: 0;
    right: 0;
    top: 314px;
    margin: 0;
    padding: 0;
    list-style: none;
    text-align: center;
    font-family: "Orbitron", sans-serif;
    font-weight: 500;
    font-size: 29px;
    line-height: 45px;
    letter-spacing: 6px;
    color: var(--accent);
  }
</style>
</head>
<body>
<main class="canvas">
  <section class="card card--front">
    <svg class="emblem" viewBox="0 0 370 370" aria-hidden="true">
      <circle cx="185" cy="185" r="179" fill="none" stroke="var(--accent)" stroke-width="10"/>
    </svg>
    <div class="emblem-name">CORVALE<br>EDIFÍCIO</div>
  </section>

  <section class="card card--back">
    <h1 class="company-name">CORVALE EDIFÍCIO INC</h1>
    <ul class="contact">
      <li class="contact-name">Owen Castell</li>
      <li class="contact-phone">555-014-2386</li>
      <li class="contact-email">corvalebuild@mail.com</li>
    </ul>
  </section>
</main>
</body>
</html>
```